Webdesign für Sexualpädagogik
Zielgruppe
- Sexualpädagogik, Beratung und Sexualtherapie
- Vorträge und Seminare für Unternehmen / Institutionen Vorträge Sexualität in der Pflege / im Alter / Grenzen wahrnehmen
- Wechseljahreberatung, Beratung in der Lebensmitte
- ZIelgruppe: Menschen, die sich weiternetwickeln möchten, die Problme mit ihrer Sexualität haben, Paare, Jugendliche
letztes Interview in der Zeitung: https://www.talbote-beispiel.ch/talbote/zeitung/frontal-interview/sexualitaet-hoert-nicht-beim-eintritt-ins-spital-auf/
Aufgabenstellung
- bestehende Internetseite siehe unten: Schrift ist Especial Key von Wolkenweg
- auf dem Briefpapier bisher noch der Fachbuchhandel und Onlinhandel, aber beides nicht mehr
- Bilder zum Thema bereist vorhanden
- für Werbeflyer habe ich die Therapie in dunkelblau gehalten udn in der sexualpädagogik in hellblau
der kramhaus wird aus der website entfernet

```html
<!DOCTYPE html>
<html lang="de">
<head>
<meta charset="utf-8">
<title>Wolkenweg – Sexualtherapie & Sexualpädagogik</title>
<link href="https://fonts.googleapis.com/css2?family=Libre+Baskerville:ital@0;1&family=Raleway:wght@400;500;600&display=swap" rel="stylesheet">
<style>
:root{
  --bg:#e4e7e3;
  --paper:#ffffff;
  --band:#ececec;
  --ink:#2b2b2b;
  --muted:#777;
  --line:#cfcfcf;
  --hero-a:#2f5f78;
  --hero-b:#c7a9a4;
  --orange:#f08a24;
  --serif:'Libre Baskerville', Georgia, serif;
  --sans:'Raleway', Arial, sans-serif;
}
*{box-sizing:border-box;margin:0;padding:0}
html,body{width:1200px;height:900px;overflow:hidden;background:var(--bg)}
body{font-family:var(--sans);color:var(--ink);display:flex;gap:18px;padding:12px 14px}
.sheet{width:378px;height:876px;background:var(--paper);box-shadow:0 2px 10px rgba(0,0,0,.15);overflow:hidden;position:relative;display:flex;flex-direction:column}
.photo{display:block}
.caps{font-size:6.5px;letter-spacing:.08em;text-transform:uppercase}
.small{font-size:7px;line-height:1.55;color:var(--muted)}
.btn{display:inline-block;border:1px solid var(--line);padding:3px 10px;font-size:6px;letter-spacing:.1em;text-transform:uppercase;margin-top:6px;color:var(--ink)}

/* header */
.site-top{display:flex;align-items:center;justify-content:space-between;padding:16px 16px 6px}
.owner{width:80px}
.owner strong{display:block;font-size:7px;font-weight:600;letter-spacing:.05em}
.owner span{font-size:6px;letter-spacing:.06em;color:var(--muted)}
.brand{font-family:var(--serif);font-size:22px;color:var(--ink)}
.nav{display:flex;flex-wrap:wrap;justify-content:center;gap:4px 7px;padding:8px 10px 10px;font-size:5px;letter-spacing:.04em;text-transform:uppercase}
.nav span{white-space:nowrap}

/* hero */
.hero{position:relative;height:230px;background:linear-gradient(120deg,var(--hero-b) 0%,#d9c2bc 35%,#7d98a6 62%,var(--hero-a) 100%)}
.hero-quote{position:absolute;right:22px;top:30px;width:190px;border:1px solid rgba(255,255,255,.6);padding:16px 14px;color:#fff;font-family:var(--serif);font-size:14px;line-height:1.35;text-align:center}
.hero-quote .btn{color:#fff;border:none;margin-top:10px}
.arrow{position:absolute;top:105px;color:#fff;font-size:14px}

/* welcome */
.welcome{background:var(--band);padding:18px 26px 54px;text-align:center}
.welcome h2{font-family:var(--serif);font-weight:400;font-size:17px;margin-bottom:8px}
.services{display:flex;gap:10px;padding:0 14px;margin-top:-40px}
.service{flex:1;position:relative}
.service .photo{height:110px}
.service .label{position:relative;margin:-10px auto 0;width:88%;background:#fff;border:1px solid var(--line);padding:5px 0;text-align:center;font-size:6px;letter-spacing:.08em;text-transform:uppercase;white-space:nowrap}
.about{padding:22px 26px;text-align:center}
.about h2{font-family:var(--serif);font-weight:400;font-size:18px;margin-bottom:10px}
.about p{font-size:7.5px;line-height:1.6;color:#444;margin-bottom:8px}

/* intro */
.intro{position:relative;padding:26px 20px 20px;background:linear-gradient(#fff 0,#fff 60%,var(--band) 60%)}
.intro .photo{height:150px;width:210px;margin-left:auto}
.intro-card{position:relative;width:210px;margin:-22px 20px 0 auto;background:#fff;border:1px solid var(--line);padding:12px 14px;text-align:center}
.intro-card h3{font-family:var(--serif);font-weight:400;font-size:13px;margin-bottom:6px}
.share{display:flex;gap:6px;justify-content:flex-end;padding:10px 30px 0}
.share span{width:9px;height:9px;border-radius:50%;background:#555}

/* blog */
.section-title{font-size:6.5px;letter-spacing:.1em;text-transform:uppercase;padding:16px 20px 8px}
.posts{display:flex;gap:14px;padding:0 20px}
.post{flex:1;text-align:center}
.post .photo{height:110px}
.post .tag{font-size:5.5px;letter-spacing:.1em;text-transform:uppercase;color:var(--muted);margin-top:8px}
.post h4{font-family:var(--serif);font-weight:400;font-size:9px;line-height:1.35;margin:4px 0}
.post .date{font-size:5.5px;color:var(--muted);margin-bottom:5px}
.post .small{text-align:justify}

.side{display:flex;gap:18px;padding:18px 20px 0}
.side-col{flex:1}
.side-item{text-align:center;margin-bottom:12px}
.side-item .photo{height:80px;margin-bottom:6px}
.side-item h5{font-family:var(--serif);font-weight:400;font-size:8.5px}
.newsletter{text-align:center}
.newsletter p{font-family:var(--serif);font-size:8px;line-height:1.45;margin:6px 0 8px}
.field{border:1px solid var(--line);height:13px;margin-bottom:5px;font-size:5.5px;color:var(--muted);padding:3px 4px;text-align:left;text-transform:uppercase;letter-spacing:.06em}

/* contact */
.contact{margin-top:auto;background:var(--band);padding:14px 18px 10px}
.contact-grid{display:flex;gap:14px}
.contact h6{font-size:7px;font-weight:600;letter-spacing:.06em;text-transform:uppercase;line-height:1.4;margin-bottom:6px}
.contact-line{display:flex;align-items:center;gap:5px;font-size:6.5px;margin-bottom:3px}
.map{height:150px;background:linear-gradient(135deg,#f3f3f3,#dfe6e8);border:1px solid var(--line);margin-top:8px}
.footer{display:flex;justify-content:flex-end;gap:16px;padding:10px 0 0;font-size:6px;letter-spacing:.1em;text-transform:uppercase}
</style>
</head>
<body>

<section class="sheet">
  <header class="site-top">
    <div class="owner"><strong>LENA MARBACH</strong><span>SEXUALTHERAPEUTIN</span></div>
    <div class="brand">Wolkenweg</div>
    <div style="width:80px"></div>
  </header>
  <nav class="nav"><span>Home</span><span>Über mich</span><span>Sexualberatung</span><span>Sexualpädagogik</span><span>Wechseljahrberatung</span><span>Seminare</span><span>Artikel</span><span>Blog</span><span>Kontakt</span></nav>
  <div class="hero" role="img" aria-label="Foto: Hände halten einen herzförmigen Stein">
    <span class="arrow" style="left:10px">‹</span><span class="arrow" style="right:10px">›</span>
    <div class="hero-quote">Wenn wir uns selbst nicht lieben, können wir auch keinen anderen Menschen lieben.<br><span class="btn">Mehr erfahren</span></div>
  </div>
  <div class="welcome">
    <h2>Wilkommen!</h2>
    <p class="small">Lorem ipsum dolor sit amet, consectetur adipiscing elit, sed do eiusmod tempor incididunt ut labore et dolore magna aliqua. Praesent elementum facilisis leo vel fringilla est ullamcorper. Duis ultricies lacus sed turpis. Ultricies mi quis hendrerit dolor magna eget est lorem.</p>
  </div>
  <div class="services">
    <div class="service"><div class="photo" role="img" aria-label="Foto: lachendes junges Paar" style="background:linear-gradient(135deg,#d8c4b6,#8c7f73)"></div><div class="label">Sexualberatung</div></div>
    <div class="service"><div class="photo" role="img" aria-label="Foto: lachende Frau mittleren Alters" style="background:linear-gradient(135deg,#e9dfd2,#b9a68e)"></div><div class="label">Wechseljahrberatung</div></div>
    <div class="service"><div class="photo" role="img" aria-label="Foto: junge Leute im Gespräch" style="background:linear-gradient(135deg,#cfd6cf,#6f7f86)"></div><div class="label">Sexualpädagogik</div></div>
  </div>
  <div class="about">
    <h2>Über Wolkenweg</h2>
    <p>Das Ziel ist die Zufriedenheit von Ihnen und Ihrem Partner. Verwirklichen Sie Ideen, Träume und Phantasien. Nutzen Sie es als Anregung für eine erfüllte und lebendige Partnerschaft und Sexualität, für ein zufriedenes und glückliches Selbst und Miteinander.</p>
    <p>Denn nur, wenn man sich selbst liebt, kann man auch die Partnerin / den Partner lieben. Verzaubern und verführen Sie mit Spass und Freude um des Verführens Willen. Die Idee basiert auf der Ganzheit der Menschen und Partnerschaft und der Individualität jeder und jedes Einzelnen.</p>
    <span class="btn">Mehr erfahren</span>
  </div>
</section>

<section class="sheet">
  <div class="intro">
    <div class="photo" role="img" aria-label="Porträtfoto der Therapeutin" style="background:linear-gradient(135deg,#e6ddd2,#a89888)"></div>
    <div class="intro-card">
      <h3>Hallo, ich bin Lena</h3>
      <p class="small">Lorem ipsum dolor sit amet, consectetur adipiscing elit, sed do eiusmod tempor incididunt ut labore et dolore magna aliqua. Praesent elementum facilisis leo vel fringilla est ullamcorper.</p>
      <span class="btn">Termin vereinbarung</span>
    </div>
    <div class="share" aria-label="Teilen"><span></span><span></span><span></span><span></span></div>
  </div>
  <div class="section-title">Aktuelles</div>
  <div class="posts">
    <article class="post">
      <div class="photo" role="img" aria-label="Foto: Frau sitzt auf einer orangen Treppe" style="background:linear-gradient(135deg,var(--orange),#e06d12)"></div>
      <div class="tag">News</div>
      <h4>Sexualität hört nicht beim Eintritt ins Spital auf</h4>
      <div class="date">26. Juli 2018</div>
      <p class="small">Vorfälle wie der sexuelle Übergriff eines Pflegers auf eine Frau im Altersheim schockieren. Allerdings sind solche Übergriffe die Ausnahme. Denn im Pflegealltag geht es meist um Nähe und Würde.</p>
      <span class="btn">Weiterlesen</span>
    </article>
    <article class="post">
      <div class="photo" role="img" aria-label="Foto: junges Paar lacht gemeinsam" style="background:linear-gradient(135deg,#d6d9d3,#6d7a80)"></div>
      <div class="tag">Seminar</div>
      <h4>Nächste Seminare: Wechseljahre – Heiss Geschüttelt, nicht kalt gerührt</h4>
      <div class="date">02. Juni 2018</div>
      <p class="small">Ein spannendes Tagesseminar über die Wechselbäder der Gefühle, über Hormone, Orientierung, Hilfen und Möglichkeiten.<br>Datum: 02.06.2018 Seminar von 9.00 – 16.00<br>Ort: Bildungshaus Lindenhof, 3930 Talhofen<br>Kosten: CHF 149.00</p>
      <span class="btn">Mehr erfahren</span>
    </article>
  </div>
</section>

<section class="sheet">
  <div class="section-title">Letzte im Blog</div>
  <div class="side">
    <div class="side-col">
      <div class="side-item"><div class="photo" role="img" aria-label="Foto: lachende Frau" style="background:linear-gradient(135deg,#eee4d6,#b8a58f)"></div><h5>Ist Liebe lernbar?</h5><div class="date small">02. Juli 2018</div></div>
      <div class="side-item"><div class="photo" role="img" aria-label="Foto: Paar im Gespräch" style="background:linear-gradient(135deg,#e3d3cb,#86776f)"></div><h5>Das Ziel und die Philosophie</h5><div class="date small">19. Juni 2018</div></div>
    </div>
    <div class="side-col newsletter">
      <div class="caps">Newsletter</div>
      <p>Sie möchten über Neuigkeiten informiert sein und / oder sind an Kursen und Weiterbildungen interessiert?</p>
      <div class="field">Name</div>
      <div class="field">E-Mail Adresse</div>
      <span class="btn">Eintragen</span>
    </div>
  </div>
  <footer class="contact">
    <div class="contact-grid">
      <div style="flex:1.2">
        <h6>Fachstelle für Sexualpädagogik<br>und Beratung</h6>
        <div class="contact-line"><svg width="7" height="9" viewBox="0 0 7 9"><path d="M3.5 0a3.3 3.3 0 0 0-3.3 3.3C.2 5.8 3.5 9 3.5 9s3.3-3.2 3.3-5.7A3.3 3.3 0 0 0 3.5 0z" fill="#333"/><circle cx="3.5" cy="3.3" r="1.2" fill="#ececec"/></svg>Gartenweg 12, 3900 Talhofen</div>
        <div class="contact-line"><svg width="8" height="8" viewBox="0 0 8 8"><path d="M1.6 0 3 1.8 2.2 2.9a5 5 0 0 0 2.9 2.9L6.2 5 8 6.4 7 8C3.2 8 0 4.8 0 1z" fill="#333"/></svg>+41 (0)70 000 12 34</div>
        <div class="contact-line"><svg width="8" height="6" viewBox="0 0 8 6"><rect width="8" height="6" fill="#333"/><path d="M0 0l4 3 4-3" stroke="#ececec" fill="none" stroke-width=".8"/></svg>info@wolkenweg.ch</div>
        <h6 style="margin-top:8px">Lageplan</h6>
        <p class="small">Vom Bahnhof zu Fuss die Hauptstrasse hinunter, bei der Kirche links und nach zweihundert Metern rechts in den Gartenweg. Parkplätze sind vor dem Haus vorhanden, der Eingang liegt hinten.</p>
        <div class="map" role="img" aria-label="Lageplan der Praxis"></div>
      </div>
      <div style="flex:1">
        <h6>Kontakt mit uns</h6>
        <div class="field">Name</div>
        <div class="field">E-Mail Adresse</div>
        <div class="field">Telefon</div>
        <div class="field" style="height:70px">Nachricht</div>
        <span class="btn">Senden</span>
      </div>
    </div>
    <div class="footer"><span>Menu</span><span>Impressum</span><span>Datenschutz</span></div>
  </footer>
</section>

</body>
</html>
```